Ravel Oversight Partners - Statonery Design

I just completed a redesign of my business card. Please do not design a logo or business card. See my current stationery design attached.

Target Market(s)

VP of Human Resources and Finance - Companies with 100 employees to 10,000

Industry/Entity Type

Business Consultant

Requirements
Must have
• Use the letterhead instructions for the color and fonts.

```html
<!DOCTYPE html>
<html lang="en">
<head>
<meta charset="utf-8">
<title>Ravel Oversight Partners – Stationery</title>
<link href="https://fonts.googleapis.com/css2?family=Bodoni+Moda:wght@400&family=Archivo+Narrow:wght@400&display=swap" rel="stylesheet">
<style>
  :root {
    --plum: #6b2a47;
    --slate: #6d6d70;
    --ink: #7a7a7c;
    --paper: #fbfbfb;
    --backdrop: #cfcfcf;
  }
  * { box-sizing: border-box; margin: 0; padding: 0; }
  html, body { width: 1200px; height: 922px; overflow: hidden; }
  body { background: var(--backdrop); position: relative; font-family: "Archivo Narrow", "Arial Narrow", sans-serif; }

  .sheet { position: absolute; background: var(--paper); box-shadow: 0 6px 18px rgba(0,0,0,.12); overflow: hidden; }
  .letterhead { left: 60px; top: 40px; width: 594px; height: 842px; }
  .envelope { left: 690px; top: 470px; width: 480px; height: 250px; }

  .edge-tab { position: absolute; width: 6px; }
  .edge-tab.plum { background: var(--plum); }
  .edge-tab.slate { background: var(--slate); }

  .brand { position: absolute; display: flex; align-items: center; gap: 10px; }
  .brand-dot { border-radius: 50%; background: var(--plum); flex: none; }
  .brand-name { font-family: "Bodoni Moda", "Didot", serif; font-weight: 400; color: var(--slate); white-space: nowrap; }
  .letterhead .brand { left: 0; right: 0; top: 112px; justify-content: center; }
  .letterhead .brand-dot { width: 26px; height: 26px; }
  .letterhead .brand-name { font-size: 23px; }
  .envelope .brand { left: 28px; top: 40px; gap: 7px; }
  .envelope .brand-dot { width: 14px; height: 14px; }
  .envelope .brand-name { font-size: 14px; }

  .letter-body { position: absolute; left: 92px; right: 92px; top: 190px; color: var(--ink); font-size: 13.5px; line-height: 1.42; }
  .letter-body p + p { margin-top: 18px; }

  .contact-line { position: absolute; display: flex; align-items: center; gap: 10px; font-family: "Bodoni Moda", serif; color: var(--slate); white-space: nowrap; }
  .contact-item { display: flex; align-items: center; gap: 3px; }
  .contact-item svg { flex: none; }
  .letterhead .contact-line { left: 22px; bottom: 46px; font-size: 10px; }
  .envelope .contact-line { left: 18px; bottom: 26px; font-size: 7.5px; gap: 7px; }

  .footer-bands { position: absolute; left: 0; width: 100%; }
  .letterhead .footer-bands { bottom: 18px; height: 22px; }
  .envelope .footer-bands { bottom: 6px; height: 16px; }
</style>
</head>
<body>

<section class="sheet letterhead" aria-label="Letterhead">
  <span class="edge-tab plum" style="left:0;top:30px;height:50px"></span>
  <span class="edge-tab slate" style="left:0;top:88px;height:50px"></span>
  <span class="edge-tab plum" style="right:0;top:170px;height:50px"></span>
  <span class="edge-tab slate" style="right:0;top:228px;height:50px"></span>

  <div class="brand">
    <span class="brand-dot"></span>
    <span class="brand-name">Ravel Oversight Partners</span>
  </div>

  <div class="letter-body">
    <p>Lorem Ipsum is simply dummy text of the printing and typesetting industry. Lorem Ipsum has been the industry's standard dummy text ever since the 1500s, when an unknown printer took a galley of type and scrambled it to make a type specimen book. It has survived not only five centuries, but also the leap into electronic typesetting, remaining essentially unchanged. It was popularised in the 1960s with the release of Lettrafix sheets containing Lorem Ipsum passages, and more recently with desktop publishing software like Pressline Composer including versions of Lorem Ipsum.</p>
    <p>It is a long established fact that a reader will be distracted by the readable content of a page when looking at its layout. The point of using Lorem Ipsum is that it has a more-or-less normal distribution of letters, as opposed to using 'Content here, content here', making it look like readable English. Many desktop publishing packages and web page editors now use Lorem Ipsum as their default model text, and a search for 'lorem ipsum' will uncover many web sites still in their infancy. Various versions have evolved over the years, sometimes by accident, sometimes on purpose (injected humour and the like).</p>
    <p>Contrary to popular belief, Lorem Ipsum is not simply random text. It has roots in a piece of classical Latin literature from 45 BC, making it over 2000 years old. Rowan Delacourt, a Latin professor at Ashgrove Hall College in Eastmere, looked up one of the more obscure Latin words, consectetur, from a Lorem Ipsum passage, and going through the cites of the word in classical literature, discovered the undoubtable source. Lorem Ipsum comes from sections 1.10.32 and 1.10.33 of "de Finibus Bonorum et Malorum" structures, to generate Lorem Ipsum which looks reasonable. The generated Lorem Ipsum is therefore always free from repetition, injected humour, or non-characteristic words etc.</p>
  </div>

  <div class="contact-line">
    <span class="contact-item"><svg width="10" height="10" viewBox="0 0 10 10"><circle cx="5" cy="5" r="5" fill="#6b2a47"/><path d="M5 2.2a1.7 1.7 0 0 0-1.7 1.7C3.3 5.2 5 7.6 5 7.6s1.7-2.4 1.7-3.7A1.7 1.7 0 0 0 5 2.2z" fill="#fff"/></svg>418 Linden Court, Suite 200, Brookfield Falls, MI 49010</span>
    <span class="contact-item"><svg width="10" height="10" viewBox="0 0 10 10"><circle cx="5" cy="5" r="5" fill="#6b2a47"/><path d="M3 3.2c.4-.4.8-.3 1 .1l.4.7c.1.3 0 .5-.2.7.3.6.7 1 1.2 1.2.2-.2.4-.3.7-.2l.7.4c.4.2.5.6.1 1-1.6 1-4.8-2.2-3.9-3.9z" fill="#fff"/></svg>555.210.4417</span>
    <span class="contact-item"><svg width="10" height="10" viewBox="0 0 10 10"><circle cx="5" cy="5" r="5" fill="#6b2a47"/><rect x="2.8" y="3.6" width="4.4" height="3" fill="#fff"/><rect x="3.6" y="2.4" width="2.8" height="1.4" fill="#fff"/></svg>555.210.4418</span>
    <span class="contact-item"><svg width="10" height="10" viewBox="0 0 10 10"><circle cx="5" cy="5" r="5" fill="#6b2a47"/><circle cx="5" cy="5" r="2.6" fill="none" stroke="#fff" stroke-width=".7"/><path d="M2.4 5h5.2M5 2.4v5.2" stroke="#fff" stroke-width=".6"/></svg>www.raveloversight.com</span>
  </div>

  <svg class="footer-bands" viewBox="0 0 594 22" preserveAspectRatio="none" aria-hidden="true">
    <rect x="0" y="0" width="594" height="3" fill="#6b2a47"/>
    <polygon points="0,6 330,6 322,10 0,10" fill="#6b2a47"/>
    <polygon points="336,6 594,6 594,10 328,10" fill="#6d6d70"/>
    <polygon points="0,13 430,13 422,22 0,22" fill="#6b2a47"/>
    <polygon points="436,13 594,13 594,22 428,22" fill="#6d6d70"/>
  </svg>
</section>

<section class="sheet envelope" aria-label="Envelope">
  <span class="edge-tab plum" style="left:0;top:28px;height:30px"></span>
  <span class="edge-tab slate" style="left:0;top:63px;height:30px"></span>
  <span class="edge-tab plum" style="right:0;top:0;height:30px"></span>
  <span class="edge-tab slate" style="right:0;top:35px;height:30px"></span>

  <div class="brand">
    <span class="brand-dot"></span>
    <span class="brand-name">Ravel Oversight Partners</span>
  </div>

  <div class="contact-line">
    <span class="contact-item"><svg width="8" height="8" viewBox="0 0 10 10"><circle cx="5" cy="5" r="5" fill="#6b2a47"/><path d="M5 2.2a1.7 1.7 0 0 0-1.7 1.7C3.3 5.2 5 7.6 5 7.6s1.7-2.4 1.7-3.7A1.7 1.7 0 0 0 5 2.2z" fill="#fff"/></svg>418 Linden Court, Suite 200, Brookfield Falls, MI 49010</span>
    <span class="contact-item"><svg width="8" height="8" viewBox="0 0 10 10"><circle cx="5" cy="5" r="5" fill="#6b2a47"/><path d="M3 3.2c.4-.4.8-.3 1 .1l.4.7c.1.3 0 .5-.2.7.3.6.7 1 1.2 1.2.2-.2.4-.3.7-.2l.7.4c.4.2.5.6.1 1-1.6 1-4.8-2.2-3.9-3.9z" fill="#fff"/></svg>555.210.4417</span>
    <span class="contact-item"><svg width="8" height="8" viewBox="0 0 10 10"><circle cx="5" cy="5" r="5" fill="#6b2a47"/><rect x="2.8" y="3.6" width="4.4" height="3" fill="#fff"/><rect x="3.6" y="2.4" width="2.8" height="1.4" fill="#fff"/></svg>555.210.4418</span>
    <span class="contact-item"><svg width="8" height="8" viewBox="0 0 10 10"><circle cx="5" cy="5" r="5" fill="#6b2a47"/><circle cx="5" cy="5" r="2.6" fill="none" stroke="#fff" stroke-width=".7"/><path d="M2.4 5h5.2M5 2.4v5.2" stroke="#fff" stroke-width=".6"/></svg>www.raveloversight.com</span>
  </div>

  <svg class="footer-bands" viewBox="0 0 480 16" preserveAspectRatio="none" aria-hidden="true">
    <rect x="0" y="0" width="480" height="2" fill="#6b2a47"/>
    <polygon points="0,4 170,4 164,7 0,7" fill="#6d6d70"/>
    <polygon points="176,4 480,4 480,7 168,7" fill="#6b2a47"/>
    <polygon points="0,10 400,10 394,16 0,16" fill="#6b2a47"/>
    <polygon points="406,10 480,10 480,16 398,16" fill="#6d6d70"/>
  </svg>
</section>

</body>
</html>
```